Promotional business a5 Notepad design

I am looking for a custom a5 notepad design as a promotional item to give away to customers etc.
Attached will be a desk planner we had designed feel free to use as a reference.
We want the notepad to have lines running horizontal not squares like the desk planner example.

Industry/Entity Type

Hydraulic / industrial

Colors

Designer to choose colors to be used in the design.

```html
<!DOCTYPE html>
<html lang="en">
<head>
<meta charset="utf-8">
<title>Coreline Hose &amp; Fittings – A5 Notepad</title>
<link href="https://fonts.googleapis.com/css2?family=Roboto:wght@400;700&display=swap" rel="stylesheet">
<style>
  :root {
    --backdrop: #e2e2e2;
    --paper: #f8f8f8;
    --brand-blue: #2c4494;
    --brand-black: #161616;
    --rule: #c8d0ea;
    --ink: #3a3a3a;
  }
  * { box-sizing: border-box; margin: 0; padding: 0; }
  html, body {
    width: 1153px; height: 1200px; overflow: hidden;
    background: var(--backdrop);
    font-family: "Roboto", sans-serif;
  }
  .notepad {
    position: absolute; left: 167px; top: 30px;
    width: 818px; height: 1140px;
    background: var(--paper);
    overflow: hidden;
  }
  .brand {
    position: absolute; left: 57px; top: 96px;
    display: flex; align-items: center; gap: 12px;
  }
  .brand-dot {
    width: 58px; height: 58px; border-radius: 50%;
    background: var(--brand-black);
  }
  .brand-name {
    font-weight: 700; font-size: 27px; color: var(--brand-blue);
    letter-spacing: 0.5px; white-space: nowrap;
  }
  .contact {
    position: absolute; left: 478px; top: 65px;
    color: var(--ink); font-size: 16px; line-height: 20px;
  }
  .contact .address { margin-bottom: 6px; }
  .contact ul { list-style: none; }
  .contact li { display: flex; align-items: center; gap: 6px; height: 21px; }
  .contact svg { width: 16px; height: 16px; fill: var(--brand-blue); flex: none; }
  .writing-lines {
    position: absolute; left: 54px; top: 239px; width: 709px;
  }
  .writing-lines span {
    display: block; height: 33.3px; border-top: 1px solid var(--rule);
  }
  .footer-band {
    position: absolute; left: 0; bottom: 0; width: 818px; height: 21px;
  }
</style>
</head>
<body>
  <main class="notepad">
    <div class="brand">
      <span class="brand-dot"></span>
      <span class="brand-name">Coreline Hose &amp; Fittings</span>
    </div>

    <address class="contact" style="font-style:normal">
      <p class="address">24 Marlow Street,<br>Kingsbury SA 5098</p>
      <ul>
        <li>
          <svg viewBox="0 0 16 16" aria-hidden="true"><path d="M1 6c0-2 3-3 7-3s7 1 7 3v1.5h-3.5V6h-7v1.5H1z"/><path d="M4 8h8l1.5 6h-11z"/><circle cx="8" cy="11" r="1.6" fill="#f8f8f8"/></svg>
          0400 123 456
        </li>
        <li>
          <svg viewBox="0 0 16 16" aria-hidden="true"><path d="M4.5 1h7a1 1 0 0 1 1 1v12a1 1 0 0 1-1 1h-7a1 1 0 0 1-1-1V2a1 1 0 0 1 1-1zm1 2v9h5V3z"/><circle cx="8" cy="13.5" r=".8" fill="#f8f8f8"/></svg>
          08 8100 2345
        </li>
        <li>
          <svg viewBox="0 0 16 16" aria-hidden="true"><path d="M1 4h14v1L8 9 1 5z"/><path d="M1 6.5l7 4 7-4V12H1z"/></svg>
          hello@corelinehose.com.au
        </li>
        <li>
          <svg viewBox="0 0 16 16" aria-hidden="true"><circle cx="8" cy="8" r="7"/><path d="M5 4c1.5 0 2 1 1.5 2S4 7 4.5 8.5 6 10 6 12L4.5 13A6 6 0 0 1 3 4.5zM10 3.5c1 .5 0 1.5 1 2s2 0 2.3 1.5c-.8 0-1.8.5-2 1.5S10 10 10.5 12l-1 1c-1-2 0-3-1-4s-1-2 0-3 1-2 1.5-2.5z" fill="#f8f8f8"/></svg>
          www.corelinehose.com.au
        </li>
      </ul>
    </address>

    <div class="writing-lines" aria-hidden="true">
      <span></span><span></span><span></span><span></span><span></span>
      <span></span><span></span><span></span><span></span><span></span>
      <span></span><span></span><span></span><span></span><span></span>
      <span></span><span></span><span></span><span></span><span></span>
      <span></span><span></span><span></span><span></span><span></span>
      <span></span>
    </div>

    <svg class="footer-band" viewBox="0 0 818 21" aria-hidden="true">
      <polygon points="0,0 595,0 572,21 0,21" fill="var(--brand-black)"/>
      <polygon points="603,0 818,0 818,21 580,21" fill="var(--brand-blue)"/>
    </svg>
  </main>
</body>
</html>
```